Shopify Website for Health & Beauty

The user must be available to answer questions quickly if there's an issue. Good communication skills require.

*These products are unisex for men & women*
www.valdoru.com

Website we like to model
https://www.lumbrivex-usa.com/
https://www.hollowmere.com/
https://www.zintock.com/

Pages:
Home, about us, contact us, affiliate, search, blog

Need to redesign my current website valdoru.com
We need a high converting website
Custom banner
Social media setup
Graphics design
Lifestyle images
Create a new Site Icon/Favicon
Custom popups
Web content
Klayivo setup for flows and custom newsletters
Create a Custom 404 Page
Set SEO Titles and Meta Descriptions
Optimize Your Site's Performance
*Set Up Your Homepage
Add metadata to all pages
Use schema markup whenever possible
Check for technical SEO errors

```html
<!DOCTYPE html>
<html lang="en">
<head>
<meta charset="utf-8">
<title>Valdoru — Health &amp; Beauty</title>
<link href="https://fonts.googleapis.com/css2?family=Montserrat:wght@400;500;600;700;800&display=swap" rel="stylesheet">
<style>
:root{
  --ink:#111111;
  --text:#333333;
  --muted:#555555;
  --red:#d63a3a;
  --line:#d9d9d9;
  --sage:#cfd6c6;
  --blog-bg:#f4f1f1;
  --dark:#1c1c1c;
  --footer:#262626;
  --white:#ffffff;
}
*{box-sizing:border-box;margin:0;padding:0}
html,body{width:1200px;height:3074px;overflow:hidden}
body{font-family:'Montserrat',sans-serif;color:var(--text);background:var(--white);position:relative}
a{color:inherit;text-decoration:none}
.abs{position:absolute}

/* top bar */
.topbar{position:absolute;top:0;left:0;width:1200px;height:39px;border-bottom:1px solid var(--line);font-size:12px;white-space:nowrap}
.topbar .mail{position:absolute;left:522px;top:0;height:39px;display:flex;gap:8px;align-items:center}
.topbar .ship{position:absolute;left:676px;top:0;height:39px;border-left:1px solid var(--line);padding-left:16px;display:flex;gap:8px;align-items:center}
.topbar .login{position:absolute;left:939px;top:0;width:62px;height:39px;background:var(--ink);color:var(--white);font-weight:700;font-size:13px;display:flex;align-items:center;justify-content:center}
.topbar .cart{position:absolute;left:1017px;top:12px;display:flex;gap:6px;align-items:center}
.topbar .cart .count{position:absolute;left:43px;top:-9px;font-size:11px}

/* nav */
.nav{position:absolute;top:39px;left:0;width:1200px;height:80px;border-bottom:1px solid var(--line)}
.logo{font-family:'Montserrat',sans-serif;font-weight:500;letter-spacing:6px;color:var(--ink)}
.nav .logo{position:absolute;left:132px;top:22px;font-size:32px}
.nav ul{list-style:none;font-size:13px;font-weight:500;color:var(--ink);white-space:nowrap}
.nav ul li{position:absolute;top:33px}
.nav ul li.active{color:var(--red)}
.search{position:absolute;left:850px;top:25px;width:219px;height:31px;border:1px solid #444;border-radius:4px;font-size:10px;padding:10px 12px;color:#333}
.search svg{position:absolute;right:9px;top:8px}

/* hero */
.hero{position:absolute;top:119px;left:0;width:1200px;height:571px;background:var(--sage)}
.hero .bottle{position:absolute;left:135px;top:80px;width:130px;height:415px;border-radius:20px;background:linear-gradient(180deg,#e7e7e7,#c9c9c9 40%,#e4d86a 60%,#dfe0dc)}
.hero .model{position:absolute;left:540px;top:28px;width:660px;height:543px;background:radial-gradient(ellipse at 55% 45%,#e4b491 0%,#c98f6a 45%,#cfd6c6 78%)}
.hero .upto{position:absolute;left:333px;top:124px;border:2px solid var(--ink);padding:8px 13px;font-size:22px;font-weight:700;color:var(--ink)}
.hero .off{position:absolute;left:330px;top:185px;font-size:64px;font-weight:800;color:var(--red)}
.hero .sub{position:absolute;left:333px;top:282px;font-size:24px;font-weight:500;color:var(--ink);line-height:35px}
.hero .shop{position:absolute;left:333px;top:379px;width:131px;height:48px;background:var(--red);color:var(--white);border-radius:4px;font-weight:700;font-size:16px;display:flex;align-items:center;justify-content:center}
.hero .arrow{position:absolute;top:260px;width:40px;height:48px;background:var(--white);display:flex;align-items:center;justify-content:center}

/* categories */
.cat{position:absolute;top:735px;width:456px;height:293px;color:var(--white)}
.cat.skin{left:131px;background:linear-gradient(90deg,#9fd4d3,#7fc2c2)}
.cat.hair{left:614px;background:linear-gradient(90deg,#b86e43,#d79a70)}
.cat h3{position:absolute;font-size:25px;font-weight:700;letter-spacing:.5px;padding-bottom:8px;border-bottom:2px solid var(--white)}
.cat.skin h3{left:58px;top:48px}
.cat.hair h3{left:33px;top:117px}

/* products */
.section-title{position:absolute;width:1200px;text-align:center;font-size:22px;font-weight:700;color:var(--ink)}
.grid{position:absolute;left:132px;top:1151px;display:grid;grid-template-columns:repeat(4,224px);column-gap:13px;row-gap:15px}
.card{height:319px;border:1px solid var(--line);text-align:center;position:relative}
.card .img{position:absolute;left:50%;transform:translateX(-50%);top:20px;height:200px;border-radius:10px}
.card .name{position:absolute;top:238px;width:100%;font-size:11px;font-weight:500;color:var(--ink);line-height:15px}
.card .price{position:absolute;top:277px;width:100%;font-size:15px;font-weight:700;color:var(--ink)}
.light{background:linear-gradient(180deg,#f0f0f0,#c8c8c8)}
.jar{background:linear-gradient(180deg,#e8e8e8,#b9c3cc)}
.darkp{background:linear-gradient(180deg,#4a4a4a,#151515)}
.gold{background:linear-gradient(180deg,#e6e6e6,#d8cf6e 60%,#d0d0d0)}
.parrow{position:absolute}

/* blog */
.blog{position:absolute;top:1861px;left:0;width:1200px;height:589px;background:var(--blog-bg)}
.blog .rule{position:absolute;left:570px;top:83px;width:60px;height:2px;background:var(--ink)}
.post{position:absolute;top:125px;width:297px;height:419px;background:var(--white);box-shadow:0 1px 4px rgba(0,0,0,.08)}
.post .ph{height:185px}
.post .date{position:absolute;left:26px;top:213px;font-size:10px;color:var(--muted)}
.post h4{position:absolute;left:26px;top:232px;right:16px;font-size:13.5px;font-weight:700;color:var(--ink);line-height:21px}
.post p{position:absolute;left:26px;right:28px;font-size:11px;line-height:17.5px;color:var(--muted)}
.post .more{position:absolute;left:27px;top:362px;width:75px;height:27px;background:var(--red);color:var(--white);font-size:9px;font-weight:700;border-radius:3px;display:flex;align-items:center;justify-content:center}

/* features */
.features{position:absolute;top:2450px;left:0;width:1200px;height:282px;background:var(--dark);color:var(--white)}
.feat{position:absolute;top:0;width:300px;text-align:center}
.feat svg{position:absolute;left:105px;top:46px}
.feat h5{position:absolute;top:173px;width:100%;font-size:16px;font-weight:700}
.feat p{position:absolute;top:208px;width:100%;font-size:11px;line-height:18px;color:#cfcfcf}

/* footer */
.footer{position:absolute;top:2732px;left:0;width:1200px;height:342px;background:var(--footer);color:var(--white)}
.footer .logo{position:absolute;left:139px;top:110px;font-size:34px;color:#e8e8e8}
.fcol h6{font-size:13px;font-weight:700;margin-bottom:27px}
.fcol ul{list-style:none;font-size:11.5px;line-height:20px;color:#ddd}
.fitem{display:flex;gap:12px;align-items:flex-start;font-size:11.5px;line-height:16px;color:#ddd;margin-bottom:21px}
.fitem .ic{width:22px;height:22px;border-radius:50%;background:var(--white);flex:none;display:flex;align-items:center;justify-content:center;margin-top:3px}
.footer .hr{position:absolute;left:132px;top:262px;width:936px;height:1px;background:#444}
.footer .copy{position:absolute;top:300px;width:1200px;text-align:center;font-size:11.5px;color:#ddd}
</style>
</head>
<body>

<header class="topbar">
  <div class="mail">
    <svg width="15" height="11" viewBox="0 0 15 11" fill="none" stroke="#333"><rect x=".5" y=".5" width="14" height="10"/><path d="M.5 .5l7 5 7-5"/></svg>
    info@valdoru.com
  </div>
  <div class="ship">
    <svg width="20" height="13" viewBox="0 0 20 13" fill="none" stroke="#333"><rect x=".5" y=".5" width="12" height="9"/><path d="M12.5 3.5h4l3 3v3h-7"/><circle cx="4" cy="11" r="1.5"/><circle cx="16" cy="11" r="1.5"/></svg>
    Free shipping on orders over $50
  </div>
  <a class="login" href="#">Login</a>
  <div class="cart">Cart
    <svg width="20" height="18" viewBox="0 0 20 18"><path d="M0 1h3l3 10h11l3-8H5" fill="none" stroke="#111" stroke-width="2"/><path d="M5 3h15l-3 8H6z" fill="#111"/><circle cx="7" cy="15" r="1.8" fill="#111"/><circle cx="16" cy="15" r="1.8" fill="#111"/></svg>
    <span class="count">0</span>
  </div>
</header>

<nav class="nav">
  <div class="logo">VALDORU</div>
  <ul>
    <li class="active" style="left:386px">HOME</li>
    <li style="left:459px">ABOUT US</li>
    <li style="left:563px">AFFILIATE</li>
    <li style="left:664px">BLOG</li>
    <li style="left:729px">CONTACT US</li>
  </ul>
  <div class="search">SEARCH
    <svg width="13" height="13" viewBox="0 0 13 13" fill="none" stroke="#333" stroke-width="1.3"><circle cx="5.5" cy="5.5" r="4.5"/><path d="M9 9l3.5 3.5"/></svg>
  </div>
</nav>

<section class="hero">
  <div class="model" role="img" aria-label="Woman with smooth skin holding her face"></div>
  <div class="bottle" role="img" aria-label="Vitamin A serum pump bottle"></div>
  <div class="upto">UP TO</div>
  <div class="off">20% OFF</div>
  <div class="sub">ON SELECT VALDORU’S<br>BRAND ITEMS</div>
  <a class="shop" href="#">SHOP NOW</a>
  <div class="arrow" style="left:0"><svg width="8" height="12" viewBox="0 0 8 12" fill="none" stroke="#333" stroke-width="1.5"><path d="M7 1L2 6l5 5"/></svg></div>
  <div class="arrow" style="left:1157px"><svg width="8" height="12" viewBox="0 0 8 12" fill="none" stroke="#333" stroke-width="1.5"><path d="M1 1l5 5-5 5"/></svg></div>
</section>

<a class="cat skin" href="#" role="img" aria-label="Skin care jar and woman with closed eyes"><h3>SKIN CARE</h3></a>
<a class="cat hair" href="#" role="img" aria-label="Hair treatment tube and woman with flowing hair"><h3>HAIR CARE</h3></a>

<h2 class="section-title" style="top:1084px">BEST PRODUCTS</h2>

<svg class="parrow" style="left:73px;top:1299px" width="14" height="24" viewBox="0 0 14 24" fill="none" stroke="#999" stroke-width="2"><path d="M12 2L2 12l10 10"/></svg>
<svg class="parrow" style="left:1109px;top:1299px" width="14" height="24" viewBox="0 0 14 24" fill="none" stroke="#999" stroke-width="2"><path d="M2 2l10 10-10 10"/></svg>
<svg class="parrow" style="left:73px;top:1622px" width="14" height="24" viewBox="0 0 14 24" fill="none" stroke="#999" stroke-width="2"><path d="M12 2L2 12l10 10"/></svg>
<svg class="parrow" style="left:1109px;top:1622px" width="14" height="24" viewBox="0 0 14 24" fill="none" stroke="#999" stroke-width="2"><path d="M2 2l10 10-10 10"/></svg>

<div class="grid">
  <div class="card"><div class="img light" style="width:50px" role="img" aria-label="Brightening vitamin C serum bottle"></div><div class="name">BRIGHTENING VITAMIN<br>C SERUM (1 OZ)</div><div class="price">$52.00</div></div>
  <div class="card"><div class="img jar" style="width:130px;height:80px;top:68px" role="img" aria-label="Brightening pads jar"></div><div class="name">DELUXE SKINCARE<br>BRIGHTENING PADS (60 PADS)</div><div class="price">$38.00</div></div>
  <div class="card"><div class="img light" style="width:66px;height:180px;top:28px" role="img" aria-label="Skin deep cleanser tube"></div><div class="name">SKIN DEEP<br>CLEANSER (4 OZ)</div><div class="price">$26.00</div></div>
  <div class="card"><div class="img gold" style="width:52px;height:180px;top:30px" role="img" aria-label="Vitamin A serum bottle"></div><div class="name">DELUXE SKINCARE<br>VITAMIN A SERUM (1 OZ)</div><div class="price">$93.60</div></div>
  <div class="card"><div class="img darkp" style="width:92px;height:170px;top:30px" role="img" aria-label="Deep treatment hair tube"></div><div class="name">DELUXE DEEP<br>TREATMENT (4 OZ)</div><div class="price">$18.59</div></div>
  <div class="card"><div class="img darkp" style="width:118px;height:90px;top:60px" role="img" aria-label="Mint pomade jar"></div><div class="name">DELUXE MINT<br>POMADE (2 OZ)</div><div class="price">$16.90</div></div>
  <div class="card"><div class="img darkp" style="width:72px;height:180px;top:28px" role="img" aria-label="Strengthening conditioner bottle"></div><div class="name">DELUXE STRENGTHENING<br>CONDITIONER (8.5 OZ)</div><div class="price">$26.39</div></div>
  <div class="card"><div class="img darkp" style="width:68px;height:195px;top:22px" role="img" aria-label="Strengthening shampoo bottle"></div><div class="name">DELUXE SKINCARE<br>VITAMIN A SERUM (1 OZ)</div><div class="price">$93.60</div></div>
</div>

<section class="blog">
  <h2 class="section-title" style="top:43px">LATEST BLOG</h2>
  <div class="rule"></div>

  <article class="post" style="left:131px">
    <div class="ph" style="background:linear-gradient(135deg,#6b3a24,#3a1e12)" role="img" aria-label="Woman with long glossy hair"></div>
    <div class="date">July 04, 2021</div>
    <h4>HOW TO HIDE OR GET RID<br>OF SPLIT ENDS?</h4>
    <p style="top:285px">Regular use of hot styling products such<br>as hair dryers, straighteners, curling irons,<br>and hot rollers has a significant influence<br>since they dehydrate the hair.</p>
    <a class="more" href="#">READ MORE</a>
  </article>

  <article class="post" style="left:453px">
    <div class="ph" style="background:linear-gradient(135deg,#efe0c9,#c9a57a)" role="img" aria-label="Hair care lotion bottles with leaves"></div>
    <div class="date">July 04, 2021</div>
    <h4>HAIR SERUM &amp; ITS BENEFITS<br>FOR YOUR HAIR</h4>
    <p style="top:285px">Best Hair Serum For Hair Growth Best<br>Keratin Serum For Hair hair care Hair<br>Care Products Online keratin serum<br>shampoo</p>
    <a class="more" href="#">READ MORE</a>
  </article>

  <article class="post" style="left:772px">
    <div class="ph" style="background:linear-gradient(135deg,#e9e4df,#9a7458)" role="img" aria-label="Woman seen from behind with wavy hair"></div>
    <div class="date">July 04, 2021</div>
    <h4>BEST SHAMPOO AND<br>CONDITIONER FOR HAIR GROWTH<br>AND STRENGTH</h4>
    <p style="top:302px">Hair Care products are a dime a dozen.<br>Everyone you know has probably tried a<br>different brand at some point.</p>
    <a class="more" href="#">READ MORE</a>
  </article>
</section>

<section class="features">
  <div class="feat" style="left:96px">
    <svg width="90" height="90" viewBox="0 0 90 90" fill="none" stroke="#fff" stroke-width="3"><path d="M45 4l8 6 10-2 4 9 9 4-2 10 6 8-6 8 2 10-9 4-4 9-10-2-8 6-8-6-10 2-4-9-9-4 2-10-6-8 6-8-2-10 9-4 4-9 10 2z"/><circle cx="45" cy="45" r="27"/><text x="45" y="44" text-anchor="middle" fill="#fff" stroke="none" font-family="Montserrat,sans-serif" font-weight="800" font-size="11">MONEY</text><text x="45" y="56" text-anchor="middle" fill="#fff" stroke="none" font-family="Montserrat,sans-serif" font-weight="800" font-size="11">BACK</text></svg>
    <h5>MONEY BACK GUARANTEE</h5>
    <p>Not satisfied with your order? Contact Us,<br>We offer no hassle returns.</p>
  </div>
  <div class="feat" style="left:450px">
    <svg width="90" height="90" viewBox="0 0 90 90" fill="none" stroke="#fff" stroke-width="3"><circle cx="45" cy="26" r="20"/><text x="45" y="35" text-anchor="middle" fill="#fff" stroke="none" font-family="Montserrat,sans-serif" font-weight="700" font-size="26">$</text><path d="M6 40v22l16 20h10V68L20 54M84 40v22L68 82H58V68l12-14"/></svg>
    <h5>SECURE PAYMENT</h5>
    <p>Your safety is our priority. All payments<br>are 100% secure.</p>
  </div>
  <div class="feat" style="left:806px">
    <svg width="90" height="90" viewBox="0 0 90 90" fill="none" stroke="#fff" stroke-width="3"><circle cx="45" cy="32" r="18"/><path d="M23 32a22 22 0 0144 0M23 30v10M67 30v10M67 40q0 12-16 12"/><path d="M8 88q4-26 37-26t37 26"/></svg>
    <h5>SUPPORT 24/7</h5>
    <p>You will speak with one of our courteous<br>representatives in 20 minutes or less.</p>
  </div>
</section>

<footer class="footer">
  <div class="logo">VALDORU</div>

  <div class="fcol abs" style="left:480px;top:52px">
    <h6>MENU</h6>
    <ul><li>HOME</li><li>ABOUT US</li><li>AFFILIATE</li><li>BLOG</li><li>CONTACT US</li></ul>
  </div>

  <div class="fcol abs" style="left:669px;top:52px">
    <h6>CONTACT US</h6>
    <div class="fitem"><span class="ic"><svg width="10" height="12" viewBox="0 0 10 12"><path d="M5 0a4 4 0 00-4 4c0 3 4 8 4 8s4-5 4-8a4 4 0 00-4-4z" fill="#262626"/><circle cx="5" cy="4" r="1.5" fill="#fff"/></svg></span><div>1480 Marlow Ridge Rd,<br>Brenton, TX 75021</div></div>
    <div class="fitem"><span class="ic"><svg width="11" height="11" viewBox="0 0 11 11"><path d="M2 0l2 3-1 1.5a6 6 0 003.5 3.5L8 7l3 2-1.5 2C5 11 0 6 0 1.5z" fill="#262626"/></svg></span><div>Call Us<br>800.555.0147</div></div>
    <div class="fitem"><span class="ic"><svg width="11" height="8" viewBox="0 0 11 8"><rect width="11" height="8" fill="#262626"/><path d="M0 0l5.5 4L11 0" stroke="#fff" fill="none"/></svg></span><div>E mail Us<br>info@valdoru.com</div></div>
  </div>

  <div class="fcol abs" style="left:961px;top:52px">
    <h6>FOLLOW US</h6>
    <div class="fitem"><span class="ic"></span><div>Like us on<br>FRIENDLOOP</div></div>
    <div class="fitem"><span class="ic"></span><div>Follow us on<br>CHIRPLINE</div></div>
    <div class="fitem"><span class="ic"></span><div>Follow us on<br>WORKNEST</div></div>
  </div>

  <div class="hr"></div>
  <div class="copy">Copyright © 2021 All Rights Reserved</div>
</footer>

</body>
</html>
```